Fashion Design Business Card

I need a new business card designed for a new fashion company. I have attached what I have currently designed. I want it more feminine looking, the logo needs to be gold. I want it simple, feminine and stylish. Please give me some different ideas with the fonts.

I need to send the design we currently have, as we have worked out the logo.
You also need all of our details
Fashion

```html
<!DOCTYPE html>
<html lang="en">
<head>
<meta charset="utf-8">
<title>Lena Marlowe – Business Card</title>
<link rel="stylesheet" href="https://fonts.googleapis.com/css2?family=Cinzel:wght@500&family=EB+Garamond&family=PT+Sans&display=swap">
<style>
  :root {
    --plum: #622061;
    --gold: #cbcb6e;
    --cream: #f3f4d4;
    --paper: #ffffff;
    --stitch: #d9c9d9;
    --ink: #5b3a5d;
  }
  html, body {
    margin: 0;
    padding: 0;
    overflow: hidden;
    background: var(--paper);
  }
  .canvas {
    position: relative;
    width: 866px;
    height: 1200px;
    overflow: hidden;
    background: var(--paper);
  }

  /* Front of card */
  .card-front {
    position: absolute;
    left: 0; top: 0;
    width: 866px; height: 509px;
    background: var(--plum);
  }
  .card-front .stitching {
    position: absolute;
    left: 15px; top: 14px; right: 15px; bottom: 16px;
    border: 2px dashed var(--stitch);
  }
  .front-mark {
    position: absolute;
    left: 0; right: 0; top: 180px;
    display: flex;
    align-items: center;
    justify-content: center;
    gap: 20px;
  }
  .front-mark .dot {
    width: 30px; height: 30px;
    border-radius: 50%;
    background: var(--gold);
  }
  .front-mark .mark-name {
    font-family: "PT Sans", sans-serif;
    font-size: 60px;
    color: var(--gold);
    line-height: 1;
  }
  .front-name {
    position: absolute;
    left: 0; right: 0; top: 364px;
    text-align: center;
    font-family: "Cinzel", serif;
    font-weight: 500;
    font-size: 48px;
    letter-spacing: 2px;
    color: var(--gold);
    line-height: 1;
  }

  /* Back of card */
  .card-back {
    position: absolute;
    left: 0; top: 690px;
    width: 866px; height: 510px;
    background: var(--cream);
  }
  .ribbon-tab {
    position: absolute;
    left: 731px; top: 0;
    width: 54px; height: 321px;
    background: var(--plum);
  }
  .ribbon-tab .stitching {
    position: absolute;
    left: 7px; right: 7px; top: 0; bottom: 8px;
    border: 2px dashed var(--stitch);
    border-top: none;
  }
  .back-name {
    position: absolute;
    left: 81px; top: 98px;
    font-family: "PT Sans", sans-serif;
    font-size: 52px;
    letter-spacing: 1px;
    color: var(--plum);
    line-height: 1;
    text-transform: uppercase;
  }
  .back-title {
    position: absolute;
    left: 84px; top: 148px;
    font-family: "EB Garamond", serif;
    font-size: 36px;
    color: var(--plum);
    line-height: 1;
  }
  .back-mark {
    position: absolute;
    left: 83px; top: 350px;
    display: flex;
    align-items: center;
    gap: 10px;
  }
  .back-mark .dot {
    width: 22px; height: 22px;
    border-radius: 50%;
    background: var(--plum);
  }
  .back-mark .mark-name {
    font-family: "PT Sans", sans-serif;
    font-size: 30px;
    color: var(--plum);
    line-height: 1;
  }
  .contact {
    position: absolute;
    right: 81px; top: 340px;
    margin: 0; padding: 0;
    list-style: none;
    text-align: right;
    font-family: "PT Sans", sans-serif;
    font-size: 25px;
    color: var(--ink);
    line-height: 36px;
  }
</style>
</head>
<body>
<div class="canvas">
  <section class="card-front">
    <div class="stitching"></div>
    <div class="front-mark">
      <span class="dot"></span>
      <span class="mark-name">Atelier Lune</span>
    </div>
    <div class="front-name">LENA MARLOWE</div>
  </section>

  <section class="card-back">
    <div class="ribbon-tab"><div class="stitching"></div></div>
    <div class="back-name">Lena&nbsp; Marlowe</div>
    <div class="back-title">fashion designer</div>
    <div class="back-mark">
      <span class="dot"></span>
      <span class="mark-name">Atelier Lune</span>
    </div>
    <ul class="contact">
      <li>0400 000 000</li>
      <li>lena@lenamarlowe.com</li>
      <li>www.lenamarlowe.com</li>
    </ul>
  </section>
</div>
</body>
</html>
```